Professionelles Design für Use Case Präsentationen im B2B-Bereich

Wir sind ein Schweizer Technologieunternehmen (Veltaro GmbH, www.veltaro-beispiel.ch), das datenbasierte Simulationen, Optimierung und Entscheidungsunterstützung für Unternehmen in Logistik, Produktion und Verkehr anbietet.
Ziel dieses Projekts ist es, bestehende Use Cases in ein modernes, visuell ansprechendes Format zu bringen, das unsere Kompetenz und den Nutzen für Kunden klar kommuniziert. Die Zielgruppe sind Entscheidungsträger in mittleren bis großen Industrieunternehmen (Bereichsleiter, Projektleiter, Geschäftsleitung).
Was wir brauchen:
– Ein cleanes, professionelles Design (PowerPoint oder PDF-Layout), das sich gut für Präsentationen, Whitepaper oder als LinkedIn-Content eignet.
– Klare Struktur mit Infografiken, Icons, Diagrammen oder Visualisierungen.
– Integration unseres Logos, Farbschemas und ggf. unseres Slogans.
Stilrichtung:
– Modern, technisch fundiert, aber nicht überladen
– Klar, direkt, seriös
– Gerne mit einem visuellen roten Faden (z. B. durchgängige Icons oder Layout-Struktur)
Ein Beispieldokument (UseCase Transportkosten) mit Inhalte ist angefügt. Ziel ist eine wiederverwendbare Vorlage, die wir für verschiedene Kunden-Use-Cases adaptieren können.
- Roboto

```html
<!DOCTYPE html>
<html lang="de">
<head>
<meta charset="utf-8">
<title>Veltaro Use Case – Transportkosten</title>
<link href="https://fonts.googleapis.com/css2?family=Montserrat:wght@600;700;800&family=Manrope:wght@400;500;700&display=swap" rel="stylesheet">
<style>
  :root{
    --bg:#231f20;
    --lime:#e0df7f;
    --ink:#111111;
    --paper:#ffffff;
    --text:#2a2a2a;
  }
  *{margin:0;padding:0;box-sizing:border-box}
  html,body{width:996px;height:1200px;overflow:hidden;background:var(--bg)}
  body{position:relative;font-family:"Manrope",sans-serif;color:var(--text)}
  .slide{position:absolute;left:50px;width:891px;height:501px;background:var(--paper);overflow:hidden}
  .slide--story{top:70px}
  .slide--result{top:618px}
  .side{position:absolute;left:0;top:0;bottom:0;background:var(--lime)}
  .slide--story .side{width:343px}
  .slide--result .side{width:346px}
  .brand{position:absolute;left:46px;top:32px;display:flex;align-items:center;gap:10px}
  .brand__dot{width:40px;height:40px;border-radius:50%;background:var(--ink)}
  .brand__name{font-family:"Montserrat",sans-serif;font-weight:800;font-size:30px;color:var(--ink);letter-spacing:.5px}
  .headline{position:absolute;left:33px;top:132px;font-family:"Montserrat",sans-serif;font-weight:700;font-size:29px;color:var(--ink);letter-spacing:-.3px;white-space:nowrap}
  .question{position:absolute;left:24px;top:224px;transform:rotate(-3deg);transform-origin:left top}
  .slide--result .question{top:212px}
  .question span{display:block;width:max-content;background:var(--paper);font-family:"Montserrat",sans-serif;font-weight:600;font-size:20px;color:var(--ink);padding:3px 12px;margin-bottom:3px;line-height:1.35;white-space:nowrap}
  .question span:nth-child(2){margin-left:4px}
  .question span:nth-child(3){margin-left:20px}
  .bars{position:absolute;left:60px;bottom:0;width:220px;height:120px}
  .bars rect{fill:var(--ink)}
  .notch{position:absolute;left:343px;width:0;height:0;border-top:6px solid transparent;border-bottom:6px solid transparent;border-left:6px solid var(--lime)}
  .block{position:absolute;left:365px;right:24px}
  .block__icon{position:absolute;left:0;top:0;width:48px;height:48px;border:2px solid var(--lime);border-radius:50%;display:flex;align-items:center;justify-content:center;background:var(--paper)}
  .block__icon svg{width:26px;height:26px}
  .block__body{margin-left:64px}
  .block__title{font-family:"Montserrat",sans-serif;font-weight:800;font-size:14px;color:var(--ink);margin-bottom:4px}
  .block__text{font-size:11px;line-height:15px}
  .benefits{list-style:none;margin-top:6px}
  .benefits li{position:relative;padding-left:21px;font-size:11px;line-height:18.7px}
  .benefits li::before{content:"";position:absolute;left:2px;top:6px;width:8px;height:8px;border-radius:50%;background:var(--lime)}
  .quote{margin-top:6px;border-left:3px solid var(--lime);padding-left:18px;padding-top:2px;padding-bottom:2px}
  .quote p{font-size:14.4px;line-height:19.5px}
  .quote strong{display:block;margin-top:8px;font-size:10.8px;font-weight:700;color:var(--ink)}
  .cta{position:absolute;left:314px;right:0;bottom:0;height:43px;background:var(--ink);clip-path:polygon(10px 0,100% 0,100% 100%,0 100%);display:flex;align-items:center;justify-content:space-between;padding:0 18px 0 18px;font-size:10px;color:var(--paper);white-space:nowrap}
  .cta__lead{color:var(--lime)}
  .cta__item{display:flex;align-items:center;gap:4px}
  .cta__item svg{width:11px;height:11px;fill:var(--paper)}
  .corner{position:absolute;fill:var(--lime)}
  .map{position:absolute;left:373px;top:32px;width:441px;height:261px;border:1px solid #9a9a9a;background:linear-gradient(135deg,#d9e2c9 0%,#c8d8b4 45%,#b9cfd8 70%,#dfe6d2 100%)}
  .dashboard{position:absolute;left:578px;top:188px;width:286px;height:284px;background:var(--paper);border:1px solid #cfcfcf;box-shadow:0 1px 3px rgba(0,0,0,.15)}
  .dashboard__title{height:28px;display:flex;align-items:center;padding-left:72px;font-size:9.5px;color:#222;border-bottom:1px solid #e3e3e3}
  .dashboard__view{position:absolute;left:4px;right:4px;top:32px;bottom:4px;background:linear-gradient(180deg,#eef0f2 0%,#e4e6ea 55%,#f3f3f3 100%)}
</style>
</head>
<body>

<section class="slide slide--story">
  <div class="side">
    <div class="brand"><span class="brand__dot"></span><span class="brand__name">Veltaro</span></div>
    <h1 class="headline">Was wäre, wenn…</h1>
    <p class="question"><span>…Sie neue Standorte mit</span><span>echten Transportkosten</span><span>vergleichen könnten?</span></p>
    <svg class="bars" viewBox="0 0 220 120" aria-hidden="true">
      <rect x="0" y="59" width="21" height="61"/><rect x="47" y="40" width="21" height="80"/>
      <rect x="93" y="25" width="21" height="95"/><rect x="139" y="7" width="21" height="113"/>
      <rect x="185" y="34" width="21" height="86"/>
    </svg>
  </div>
  <span class="notch" style="top:44px"></span>
  <span class="notch" style="top:127px"></span>
  <span class="notch" style="top:224px"></span>
  <span class="notch" style="top:357px"></span>

  <article class="block" style="top:32px">
    <div class="block__icon"><svg viewBox="0 0 24 24"><circle cx="12" cy="12" r="10" fill="#111"/><path d="M7.5 12.3l3 3 6-6.3" fill="none" stroke="#fff" stroke-width="2.2" stroke-linecap="round" stroke-linejoin="round"/></svg></div>
    <div class="block__body">
      <h2 class="block__title">Ausgangslage &amp; Ziel</h2>
      <p class="block__text">Ein Handelsunternehmen prüfte mehrere neue Standorte. Dabei ging es um die Frage: Wie verändern sich die Transportkosten und die Kundenbelieferung bei einem Umzug?</p>
    </div>
  </article>

  <article class="block" style="top:115px">
    <div class="block__icon"><svg viewBox="0 0 24 24"><path d="M12 3v4M5 6l3 3M19 6l-3 3M4 13h3M17 13h3" stroke="#111" stroke-width="1.6" stroke-linecap="round"/><path d="M9 10h6l-1 5v5h-4v-5z" fill="#111"/></svg></div>
    <div class="block__body">
      <h2 class="block__title">Die Lösung – Unsere Simulation</h2>
      <p class="block__text">Wir kombinierten Standortdaten, Kundenadressen und Liefermengen mit einem automatisierten Tourenplaner. So wurden die neuen Transportkosten und Fahrzeiten für alle Varianten berechnet und visualisiert.</p>
    </div>
  </article>

  <article class="block" style="top:208px">
    <div class="block__icon" style="top:7px"><svg viewBox="0 0 24 24"><path d="M12 2a7 7 0 0 0-7 7c0 5 7 13 7 13s7-8 7-13a7 7 0 0 0-7-7z" fill="#111"/><circle cx="12" cy="9" r="2.6" fill="#fff"/></svg></div>
    <div class="block__body">
      <h2 class="block__title">Der konkrete Nutzen</h2>
      <ul class="benefits">
        <li>Vergleich der Standorte mit echten Touren</li>
        <li>Transparente Berechnung der Transportkosten</li>
        <li>Klare Entscheidungsgrundlage für Geschäftsleitung</li>
        <li>Erste Resultate in weniger als 3 Wochen</li>
      </ul>
    </div>
  </article>

  <article class="block" style="top:340px">
    <div class="block__icon" style="top:4px"><svg viewBox="0 0 24 24"><path d="M4 6h13a2 2 0 0 1 2 2v7a2 2 0 0 1-2 2H9l-4 3v-3H4a2 2 0 0 1-2-2V8a2 2 0 0 1 2-2z" fill="#111"/><path d="M6 10h7M6 13h5" stroke="#fff" stroke-width="1.4" stroke-linecap="round"/><path d="M20 1l.9 1.9 2 .3-1.5 1.4.4 2-1.8-1-1.8 1 .4-2-1.5-1.4 2-.3z" fill="#111"/></svg></div>
    <div class="block__body">
      <h2 class="block__title">Kundenfeedback</h2>
      <div class="quote">
        <p>Wir wussten genau, welcher Standort für unsere Kundenbelieferung am effizientesten ist</p>
        <strong>datenbasiert und nachvollziehbar.“</strong>
      </div>
    </div>
  </article>

  <footer class="cta">
    <span><span class="cta__lead">Jetzt testen:</span> Standortentscheidung absichern mit Simulation</span>
    <span class="cta__item"><svg viewBox="0 0 24 24"><path d="M6.6 10.8a15 15 0 0 0 6.6 6.6l2.2-2.2a1 1 0 0 1 1-.25 11.4 11.4 0 0 0 3.6.57 1 1 0 0 1 1 1V20a1 1 0 0 1-1 1A17 17 0 0 1 3 4a1 1 0 0 1 1-1h3.5a1 1 0 0 1 1 1c0 1.25.2 2.45.57 3.6a1 1 0 0 1-.25 1z"/></svg>+41 00 000 00 00</span>
    <span class="cta__item"><svg viewBox="0 0 24 24"><path d="M2 5h20v14H2z" fill="none" stroke="#fff" stroke-width="2"/><path d="M2 5l10 8 10-8" fill="none" stroke="#fff" stroke-width="2"/></svg>info@veltaro-beispiel.ch</span>
  </footer>
</section>

<section class="slide slide--result">
  <div class="side">
    <div class="brand"><span class="brand__dot"></span><span class="brand__name">Veltaro</span></div>
    <h2 class="headline">Was wäre, wenn…</h2>
    <p class="question"><span>…Sie neue Standorte mit</span><span>echten Transportkosten</span><span>vergleichen könnten?</span></p>
    <svg class="bars" viewBox="0 0 220 120" aria-hidden="true">
      <rect x="3" y="59" width="21" height="61"/><rect x="49" y="40" width="21" height="80"/>
      <rect x="96" y="26" width="21" height="94"/><rect x="142" y="7" width="21" height="113"/>
      <rect x="188" y="34" width="21" height="86"/>
    </svg>
  </div>
  <svg class="corner" style="left:828px;top:0;width:63px;height:62px" viewBox="0 0 63 62" aria-hidden="true"><polygon points="0,0 63,0 63,62"/></svg>
  <svg class="corner" style="left:698px;top:313px;width:193px;height:188px" viewBox="0 0 193 188" aria-hidden="true"><polygon points="193,0 193,188 0,188"/></svg>

  <div class="map" role="img" aria-label="Karte der Schweiz mit Lagerstandorten und farbigen Kundenpunkten der Touren"></div>
  <div class="dashboard">
    <div class="dashboard__title">Beispiel Tourenplanung Auswertung</div>
    <div class="dashboard__view" role="img" aria-label="Dashboard-Auswertung mit Kennzahlen, Tourenkarte, Tabelle und Diagrammen zu Fahrdistanz und Auslastung"></div>
  </div>
</section>

</body>
</html>
```